Fat Loss Specialist Personal Training

I need a flyer which is of a high professional standard and looks to the customer that it represents my business as a quality company. I am a personal trainer who specialises in Fat Loss and want this to be the main focus of the flyer. My business is called Summit Sculpt. Please have a look at my website to see what I offer - www.summit-sculpt.co.uk . On the flyer I want it to show what I offer such as one to one PT, nutrition plans etc. A5 Size Flyer.

Target Market(s)

Women

Industry/Entity Type

Business

Font styles to use
Other font styles liked:
• Arial

Requirements
Must have
• Personal Training
• Fat Loss Specialist
• Summit Sculpt Logo on it (my business)
• My details needs to be on it -
• Contact number - 07493021568
• Email - dan@summit-sculpt.co.uk
Nice to have
• Motivating to the customer
• Well presented
• High quality flyer
• Friendly approach
• Follow the same colour scheme as my website
Should not have
• No swear words
• No blurry images / texts

```html
<!DOCTYPE html>
<html lang="en">
<head>
<meta charset="utf-8">
<title>Summit Sculpt – Fat Loss Specialist Personal Training</title>
<link rel="stylesheet" href="https://fonts.googleapis.com/css2?family=Arimo:ital,wght@0,400;0,700;1,400;1,700&family=Open+Sans:wght@400&display=swap">
<style>
  :root {
    --band: #000000;
    --panel: #d6d6d6;
    --ink: #111111;
    --white: #ffffff;
    --muted: #8a8a8a;
    --rule: #1a1a1a;
    --pill-top: #8c8c8c;
    --pill-mid: #3a3a3a;
    --pill-bottom: #111111;
    --photo-a: #6d6a6a;
    --photo-b: #2c2a2c;
  }
  * { margin: 0; padding: 0; box-sizing: border-box; }
  html, body { width: 1200px; height: 845px; overflow: hidden; background: var(--band); }
  .flyer {
    position: relative; width: 1200px; height: 845px;
    font-family: "Arimo", Arial, sans-serif; color: var(--ink);
    background: var(--panel); overflow: hidden;
  }
  .masthead {
    position: absolute; left: 0; top: 0; width: 1200px; height: 186px;
    background: var(--band);
  }
  .brand-name {
    position: absolute; left: 528px; top: 30px;
    font-family: "Open Sans", Arial, sans-serif; font-weight: 400;
    font-size: 80px; letter-spacing: -1px; color: var(--white); white-space: nowrap;
  }
  .tagline {
    position: absolute; right: 40px; top: 128px;
    font-style: italic; font-size: 23px; color: var(--muted); white-space: nowrap;
  }
  .tagline strong { font-weight: 400; color: var(--white); }

  .intro { position: absolute; left: 56px; top: 228px; width: 712px; }
  .headline { font-size: 25.5px; font-weight: 700; line-height: 38px; }
  .lead { margin-top: 14px; font-size: 21.5px; line-height: 38px; }
  .lead strong { font-weight: 700; }

  .rule { position: absolute; left: 56px; width: 712px; height: 2px; background: var(--rule); }
  .rule.top { top: 442px; }
  .rule.bottom { top: 675px; }

  .services { position: absolute; left: 48px; top: 466px; list-style: none; }
  .service { display: flex; align-items: center; height: 32px; margin-bottom: 18.5px; }
  .pill {
    width: 207px; height: 32px; border-radius: 16px;
    background: linear-gradient(to bottom, var(--pill-top) 0%, var(--pill-mid) 45%, var(--pill-bottom) 100%);
    border: 1px solid #000;
    color: var(--white); font-weight: 700; font-size: 25px; line-height: 30px;
    padding-left: 15px; text-shadow: 1px 1px 1px #000;
  }
  .service-desc { margin-left: 27px; font-size: 25.5px; white-space: nowrap; }

  .photo { position: absolute; }
  .photo.action {
    left: 595px; top: 466px; width: 168px; height: 188px;
    background: linear-gradient(160deg, var(--photo-a), var(--photo-b));
  }
  .photo.portrait {
    left: 850px; top: 232px; width: 306px; height: 321px;
    background: linear-gradient(180deg, #b9c3cf 0%, #8d8f96 45%, #1f1f22 100%);
  }

  .cta { position: absolute; left: 56px; top: 692px; font-size: 21.5px; }

  .divider { position: absolute; left: 810px; top: 232px; width: 2px; height: 480px; background: var(--rule); }

  .quote {
    position: absolute; right: 44px; top: 574px; text-align: right;
    font-style: italic; font-size: 30px; line-height: 38px;
  }
  .quote-author {
    position: absolute; right: 58px; top: 697px;
    font-style: italic; font-weight: 700; font-size: 18px;
  }

  .contact-bar {
    position: absolute; left: 0; top: 738px; width: 1200px; height: 107px;
    background: var(--band); color: var(--white);
    font-size: 30px; display: flex; align-items: center; padding-left: 50px;
  }
  .contact-item { white-space: nowrap; }
  .contact-item b { font-weight: 700; margin-right: 6px; }
  .contact-item.email { width: 476px; }
  .contact-item.web { width: 402px; }
</style>
</head>
<body>
<div class="flyer">
  <header class="masthead">
    <div class="brand-name">Summit Sculpt</div>
    <p class="tagline">Fat Loss Specialist <strong>Personal Training</strong></p>
  </header>

  <section class="intro">
    <h1 class="headline">One to One training - Personal Training is the way forward if you want quick, effective results.</h1>
    <p class="lead">Here at <strong>Summit Sculpt</strong>, we put every ounce of passion into our clients where we achieve results in efficient time with the results effective.</p>
  </section>

  <div class="rule top"></div>

  <ul class="services">
    <li class="service"><span class="pill">Fat Loss</span><span class="service-desc">Get Lean, Burn Fat</span></li>
    <li class="service"><span class="pill">Muscle Gain</span><span class="service-desc">Build Size and Strength</span></li>
    <li class="service"><span class="pill">Tone</span><span class="service-desc">Body Definition</span></li>
    <li class="service"><span class="pill">Nutrition</span><span class="service-desc">Eat Well, Eat Clean</span></li>
  </ul>

  <div class="photo action" role="img" aria-label="Photo of the trainer working out on gym equipment"></div>

  <div class="rule bottom"></div>
  <p class="cta">Contact us for details about our tailored programmes.</p>

  <div class="divider"></div>

  <div class="photo portrait" role="img" aria-label="Portrait photo of the trainer standing with arms folded in the gym"></div>

  <blockquote class="quote">"I will get you results,<br>you will get your<br>Summit Sculpt!"</blockquote>
  <p class="quote-author">Dan Harwell</p>

  <footer class="contact-bar">
    <span class="contact-item email"><b>e</b>dan@summit-sculpt.co.uk</span>
    <span class="contact-item web"><b>w</b>summit-sculpt.co.uk</span>
    <span class="contact-item phone"><b>t</b>07493021568</span>
  </footer>
</div>
</body>
</html>
```